Sexy Flyer for Bra Sale

We a need flyer designed for promoting the brand Tarvel Apparel Company which has just begun selling bra's. need a flyer which can posted on Facebook and other social media websites. the flyer has to be attractive to girls/ladies between the ages 16 - 39. The company has been associated mainly with men's products and is now venturing into supplying bra's into the market. The tarvel company logo, the bra label design and the pictures of the bra's are attached.

Product description
Microfiber T-shirt bra with molded, lightly padded underwire cups for shaping and good support the bra also give's a fuller, uplifted shape and enhanced cleavage . Invisible seams for improved comfort. Narrow, adjustable shoulder straps and hook-and-eye fasteners at back. Available in two colors of Black & Black with Decorative Touches of Pink.

About Tarvel Apparel Company
The Tarvel Apparel Company was founded on the philosophy of design, quality and the ideals of redefining fashion. Sri Lanka is the global hub for manufacturing some of the most exclusive and fashionable products and the Tarvel brand aims at giving the Sri Lankan consumer access to high-quality, affordable and fashionable clothing from a trusted company and name. A company-wide devotion to high quality‚ honest values and timeless style with a twist. That’s authentic Tarvel. And that’s just what you’ll get‚ no matter your latitude or longitude. At Tarvel Apparel Company we constantly strive to build a culture just as inspiring as the people who wear our clothes…

Target Market(s)

Ladies Girls 16 -39
Selling Bra's

Industry/Entity Type

Womens Clothing

Requirements
Must have
• To be able to upload the flyer on Facebook and other social media platforms
• the flyer must include the Tarvel Apparel Company Logo
Nice to have
• Sexy flyer.

```html
<!DOCTYPE html>
<html lang="en">
<head>
<meta charset="utf-8">
<title>Tarvel Apparel Company – Women Lingerie Discount Vouchers</title>
<link rel="stylesheet" href="https://fonts.googleapis.com/css2?family=Abril+Fatface&family=Raleway:wght@300;600;700;800&family=Lato:wght@400&display=swap">
<style>
  :root {
    --ink: #0a0a0a;
    --paper: #f0f0f0;
    --white: #ffffff;
    --photo-light: #cfcdcb;
    --photo-mid: #a7a4a2;
    --photo-warm: #b58c72;
    --denim: #8fa6c0;
    --brand-grey: #66626a;
  }
  * { margin: 0; padding: 0; box-sizing: border-box; }
  html, body { width: 1200px; height: 589px; overflow: hidden; background: var(--white); }
  .flyer { position: relative; width: 1200px; height: 589px; overflow: hidden; }

  .panel { position: absolute; top: 0; height: 589px; }
  .panel--photo { left: 0; width: 398px;
    background: linear-gradient(160deg, var(--photo-light) 0%, var(--photo-mid) 40%, var(--photo-warm) 62%, var(--denim) 100%); }
  .panel--title { left: 398px; width: 194px; background: var(--paper); }
  .panel--results { left: 592px; width: 192px; background: var(--ink); }
  .panel--offer { left: 784px; width: 195px; background: var(--paper); }
  .panel--flat { left: 979px; width: 221px; background: var(--ink); }

  .brand-name {
    position: absolute; left: 246px; top: 500px; width: 146px;
    font-family: "Raleway", sans-serif; font-weight: 700;
    font-size: 22px; line-height: 24px; color: var(--brand-grey);
    text-align: center;
  }

  .headlines { position: absolute; left: 0; top: 0; }
  .sans-head { font-family: "Raleway", sans-serif; font-weight: 800; fill: var(--ink); }
  .display { font-family: "Abril Fatface", serif; }
  .display--dark { fill: var(--ink); }
  .display--light { fill: var(--white); }

  .copy {
    position: absolute; font-family: "Lato", sans-serif; font-size: 10.4px;
    line-height: 13px; color: var(--white); text-align: justify; hyphens: auto;
  }
  .copy p + p { margin-top: 17px; }
  .copy--results { left: 610px; top: 199px; width: 159px; }
  .copy--flat { left: 1000px; top: 221px; width: 158px; }

  .tagline {
    position: absolute; left: 1003px; top: 70px;
    font-family: "Raleway", sans-serif; font-weight: 300;
    font-size: 25px; line-height: 28px; color: var(--white); letter-spacing: 0.2px;
  }
  .tagline strong { font-weight: 700; }
</style>
</head>
<body>
<main class="flyer">
  <div class="panel panel--photo" role="img" aria-label="Photograph of a model in ripped blue jeans lying against a grey wall"></div>
  <div class="panel panel--title"></div>
  <div class="panel panel--results"></div>
  <div class="panel panel--offer"></div>
  <div class="panel panel--flat"></div>

  <div class="brand-name">Tarvel Apparel Company</div>

  <svg class="headlines" width="1200" height="589" viewBox="0 0 1200 589" aria-hidden="false">
    <text class="sans-head" font-size="61" transform="translate(488 532) rotate(-90)"
          textLength="480" lengthAdjust="spacingAndGlyphs">WOMEN LINGERIE</text>
    <text class="display display--dark" font-size="60" transform="translate(554 532) rotate(-90)"
          textLength="392" lengthAdjust="spacingAndGlyphs">DISCOUNT VOUCHERS</text>

    <text class="display display--light" font-size="90" x="604" y="148"
          textLength="154" lengthAdjust="spacingAndGlyphs">100%</text>
    <text class="display display--light" font-size="42" x="604" y="182"
          textLength="120" lengthAdjust="spacingAndGlyphs">RESULTS</text>

    <text class="display display--dark" font-size="60" transform="translate(868 496) rotate(-90)"
          textLength="236" lengthAdjust="spacingAndGlyphs">50 % OFFER</text>
    <text class="display display--dark" font-size="60" transform="translate(934 496) rotate(-90)"
          textLength="396" lengthAdjust="spacingAndGlyphs">DISCOUNT VOUCHERS</text>

    <text class="display display--light" font-size="86" x="1006" y="472"
          textLength="118" lengthAdjust="spacingAndGlyphs">10%</text>
    <text class="display display--light" font-size="44" x="1036" y="510"
          textLength="68" lengthAdjust="spacingAndGlyphs">FLAT</text>
    <text class="display display--light" font-size="44" x="1006" y="544"
          textLength="130" lengthAdjust="spacingAndGlyphs">DISCOUNT</text>
  </svg>

  <div class="copy copy--results">
    <p>Lorem ipsum dolor sit mero moleamet, soluta euismod his ea, hiea munere accusamus ullamco detore rper quo, utamur signiferumque et duo. Brute inani in pro, in est audire delicata. Eos rebum dicant constituto ex, vix hinc postea molestiae ne, nam an fugit probatus suscipiantu50%</p>
    <p>offr. Dicit quaestio principes ieum ex, id est alia scriptorem definitiones. Assum legimusreferrentur nam utaudire delicata. Eos rebum dicant constituto ex, vix hinc postea molestiae ne, nam an fugit probatus suscipiantur. Dicit quaestio principes ieum ex, id est alia scriptorem definitiones. Assum</p>
  </div>

  <div class="tagline">
    <strong>BUSINESS</strong><br>
    INSPIRATION<br>
    METION<br>
    <strong>TORNA YKSI</strong><br>
    VOUCHER TO
  </div>

  <div class="copy copy--flat">
    <p>Lorem ipsum dolor sit mero moleamet, soluta euismod his ea, hiea munere accusamus ullamco detore rper quo, utamur signiferumque et duo. Brute inani in pro, in est audire delicata. Eos rebum dicant constituto ex, vix hinc postea molestiae ne, nam an fugit probatus suscipiantu50%</p>
  </div>
</main>
</body>
</html>
```